Upscale business cards needed for family office

We would like professional business cards created for employees of our family office. Relatively simple and straightforward, but also with a unique element to set them apart. Probably stick with neutral and simple colors that mesh well with the colors in the logo. We need space for the traditional elements, including name, title, address, email/phone number.

Industry/Entity Type

Business

Contact Information for Business Card

Space for name, title, phone number, email, address

```html
<!DOCTYPE html>
<html lang="en">
<head>
<meta charset="utf-8">
<title>H&amp;W LLC – Business Card</title>
<link rel="stylesheet" href="https://fonts.googleapis.com/css2?family=Andada+Pro:wght@400;700&display=swap">
<style>
  :root {
    --paper: #ffffff;
    --ink-grey: #6b6b6b;
    --ink-blue: #3d6db5;
    --rule-grey: #7a7a7a;
  }
  * { margin: 0; padding: 0; box-sizing: border-box; }
  html, body {
    width: 1200px;
    height: 720px;
    overflow: hidden;
    background: var(--paper);
  }
  .card {
    position: relative;
    width: 1200px;
    height: 720px;
    background: var(--paper);
    font-family: "Andada Pro", Georgia, serif;
    color: var(--ink-grey);
  }
  .brand-area {
    position: absolute;
    left: 131px;
    top: 190px;
    width: 295px;
    height: 325px;
    display: flex;
    align-items: center;
    justify-content: center;
  }
  .brand-name {
    font-weight: 700;
    font-size: 50px;
    line-height: 1;
    color: var(--ink-grey);
    white-space: nowrap;
  }
  .divider {
    position: absolute;
    left: 547px;
    top: 186px;
    width: 4px;
    height: 336px;
    background: linear-gradient(to bottom, rgba(122,122,122,0), var(--rule-grey) 8%, var(--rule-grey) 92%, rgba(122,122,122,0));
  }
  .details {
    position: absolute;
    left: 657px;
    top: 172px;
  }
  .person-name {
    font-size: 46px;
    font-weight: 400;
    color: var(--ink-blue);
    line-height: 1.1;
    letter-spacing: 0.5px;
  }
  .role, .company {
    font-size: 30px;
    line-height: 46px;
  }
  .role { margin-top: 4px; }
  .address {
    margin-top: 12px;
    font-size: 30px;
    line-height: 47px;
    font-style: normal;
  }
  .contact-list {
    list-style: none;
    margin-top: 2px;
  }
  .contact-item {
    display: flex;
    align-items: center;
    font-size: 30px;
    line-height: 48px;
    white-space: nowrap;
  }
  .contact-icon {
    width: 28px;
    height: 28px;
    margin-right: 26px;
    flex: none;
  }
  .contact-icon path, .contact-icon rect {
    fill: none;
    stroke: var(--ink-blue);
    stroke-width: 2.4;
    stroke-linejoin: round;
    stroke-linecap: round;
  }
  .phone-number { margin-left: 6px; word-spacing: 4px; }
</style>
</head>
<body>
  <main class="card">
    <div class="brand-area">
      <span class="brand-name">H&amp;W LLC</span>
    </div>

    <div class="divider" aria-hidden="true"></div>

    <section class="details">
      <h1 class="person-name">DANIEL HART</h1>
      <p class="role">Director</p>
      <p class="company">H&amp;W LLC</p>
      <address class="address">
        2816 Harbor Crest Ave.<br>
        Portland OR 97201
      </address>
      <ul class="contact-list">
        <li class="contact-item">
          <svg class="contact-icon" viewBox="0 0 28 28" aria-hidden="true">
            <path d="M7 4 L11 4 L12.5 9.5 L10 11.5 C11.5 15.5 13 17.5 16.5 19.5 L18.5 17 L24 18.5 L24 22.5 C24 23.5 23 24.5 21.5 24.2 C12.5 22.5 6 15.5 4.5 6.5 C4.3 5 5.5 4 7 4 Z"/>
          </svg>
          <span class="phone-number">+330 5182-4096</span>
        </li>
        <li class="contact-item">
          <svg class="contact-icon" viewBox="0 0 28 28" aria-hidden="true">
            <rect x="3" y="7" width="22" height="15" rx="2"/>
            <path d="M4 8.5 L14 15.5 L24 8.5"/>
          </svg>
          <span class="email">info@danielhart.com</span>
        </li>
      </ul>
    </section>
  </main>
</body>
</html>
```